Premium Food Label Design – High-End Boutique Jar Labels (3 Sizes)

I require a complete jar label redesign across three sizes:
75mm x 130mm (Large & Medium)
55mm x 120mm (Small)
45mm x 120mm (XS)

The design must feel professional, modern, elegant, and high-end boutique.
Primary aesthetic: white, minimal, refined, with accents in soft brown and gold/bronze. (see prefer colours of logo in OLD LABEL PDF)
Transparent background required.

I have attached my current label for wording reference only — I want to move away from the kraft look entirely.
The label must include all existing details, plus a dedicated space to manually add batch number and date.

IMPORTANT: Final files must be supplied as editable Adobe Illustrator (.AI) files with live text layers (not outlined) so I can update them as needed.
Logo is attached. I’m open to a fresh, elevated design direction aligned with a premium brand feel.
Updates

Low design quality

Target Market(s)

People who appreciate high-end, thoughtfully crafted food and are willing to pay for quality

Industry/Entity Type

Gourmet Food / Artisan Food Packaging

Requirements
Must have
• Premium, minimal aesthetic, Strong typography hierarchy, White background, Consistency across 3 sizes
Nice to have
• Elevated “Amber Meadow” styling
Should not have
• No bright or bold colours, No clutter or overcrowding, No heavy borders or thick frames,No “homemade/craft” fonts

```html
<!DOCTYPE html>
<html lang="en">
<head>
<meta charset="utf-8">
<title>Tomato Relish – Label Concepts 4 and 5</title>
<link rel="stylesheet" href="https://fonts.googleapis.com/css2?family=Poppins:wght@300;700&family=Lustria&family=Cormorant+Garamond:ital,wght@0,500;1,500&display=swap">
<style>
  :root {
    --canvas: #ffffff;
    --label: #f6f6f6;
    --ink: #3a3a3a;
    --ink-soft: #8a8a8a;
    --accent-red: #e8121b;
    --produce-terracotta: #b9786a;
    --produce-cream: #e6dccb;
    --produce-blush: #d2b3ad;
    --produce-sage: #a7b38f;
  }
  * { box-sizing: border-box; margin: 0; padding: 0; }
  html, body { width: 1200px; height: 892px; overflow: hidden; background: var(--canvas); }
  .board { position: relative; width: 1200px; height: 892px; }

  .concept-heading {
    position: absolute; top: 32px; width: 426px;
    text-align: center; color: var(--accent-red);
    font-family: "Poppins", sans-serif;
  }
  .concept-heading .concept-number { font-weight: 700; font-size: 26px; line-height: 32px; display: block; }
  .concept-heading .concept-note { font-weight: 300; font-size: 26px; line-height: 36px; display: block; letter-spacing: 0.5px; }
  .heading-4 { left: 128px; }
  .heading-5 { left: 634px; }

  .label {
    position: absolute; top: 112px; width: 426px; height: 736px;
    background: var(--label); color: var(--ink);
  }
  .label-4 { left: 128px; }
  .label-5 { left: 627px; }

  .label-art { position: absolute; left: 0; top: 0; }

  .brand-name {
    position: absolute; width: 100%; text-align: center;
    font-family: "Lustria", serif; color: var(--ink);
  }
  .label-4 .brand-name { top: 184px; font-size: 29px; letter-spacing: 0.5px; }

  .product-name {
    position: absolute; width: 100%; text-align: center;
    font-family: "Lustria", serif; font-weight: 400; color: var(--ink); line-height: 1;
  }
  .label-4 .product-name { top: 264px; font-size: 56px; }
  .label-4 .product-name span { display: block; margin-bottom: 6px; }
  .label-5 .product-name { top: 138px; left: 10px; font-size: 72px; }
  .label-5 .product-name span { display: block; margin-bottom: 8px; }

  .produce-visual {
    position: absolute; left: 24px; top: 392px; width: 380px; height: 164px;
    border-radius: 70px 70px 50px 50px;
    background: radial-gradient(ellipse at 22% 50%, var(--produce-cream) 0 20%, transparent 42%),
                radial-gradient(ellipse at 52% 58%, var(--produce-blush) 0 18%, transparent 40%),
                radial-gradient(ellipse at 80% 48%, var(--produce-terracotta) 0 14%, transparent 36%),
                radial-gradient(ellipse at 40% 28%, var(--produce-terracotta) 0 10%, transparent 30%),
                linear-gradient(180deg, #ece4dc 0%, #e4d6cc 60%, var(--produce-sage) 100%);
    opacity: 0.8;
  }

  .claim-badge {
    position: absolute; left: 33px; top: 515px; width: 128px; height: 128px;
    display: flex; align-items: center; justify-content: center; text-align: center;
    font-family: "Lustria", serif; font-size: 18px; line-height: 19px; color: var(--ink);
  }

  .logo-spot { position: absolute; left: 0; width: 100%; text-align: center; }
  .logo-spot .logo-dot {
    display: block; margin: 0 auto 16px; width: 40px; height: 40px;
    border-radius: 50%; background: var(--ink);
  }
  .logo-spot .logo-name {
    font-family: "Lustria", serif; font-size: 28px; letter-spacing: 4px; color: var(--ink);
  }
  .label-5 .logo-spot { top: 500px; }

  .batch-field {
    position: absolute; top: 660px; width: 100%;
    display: flex; justify-content: center; gap: 22px;
    font-family: "Poppins", sans-serif; font-weight: 300; font-size: 10px;
    letter-spacing: 1.5px; color: var(--ink-soft);
  }
  .batch-field .field-line {
    display: inline-block; width: 70px; margin-left: 6px;
    border-bottom: 1px solid var(--ink-soft); vertical-align: -2px;
  }

  .tagline {
    position: absolute; top: 692px; width: 100%; text-align: center;
    font-family: "Cormorant Garamond", serif; font-style: italic; font-weight: 500;
    font-size: 22px; color: var(--ink);
  }
  .tagline .heart { font-style: normal; font-size: 17px; }
</style>
</head>
<body>
<main class="board">

  <h2 class="concept-heading heading-4">
    <span class="concept-number">CONCEPT - 4</span>
    <span class="concept-note">(TRANSPARENT LABEL)</span>
  </h2>
  <h2 class="concept-heading heading-5">
    <span class="concept-number">CONCEPT - 5</span>
    <span class="concept-note">(TRANSPARENT LABEL)</span>
  </h2>

  <section class="label label-4">
    <svg class="label-art" width="426" height="736" viewBox="0 0 426 736">
      <path d="M42 138 L48 252 L378 252 L384 138 Q300 132 260 108 Q213 70 166 108 Q126 132 42 138 Z"
            fill="none" stroke="var(--ink)" stroke-width="1.6"/>
      <path d="M50 145 L55 244 L371 244 L376 145 Q296 140 256 116 Q213 82 170 116 Q130 140 50 145 Z"
            fill="none" stroke="var(--ink)" stroke-width="1"/>
      <path d="M80 256 Q66 330 78 420" fill="none" stroke="var(--ink)" stroke-width="1.6"/>
      <path d="M346 256 Q360 330 348 420" fill="none" stroke="var(--ink)" stroke-width="1.6"/>
      <rect x="104" y="150" width="64" height="18" rx="9" fill="var(--ink-soft)" opacity="0.22"
            role="img" aria-label="Decorative flourish"/>
      <rect x="258" y="150" width="64" height="18" rx="9" fill="var(--ink-soft)" opacity="0.22"
            role="img" aria-label="Decorative flourish"/>
      <circle cx="213" cy="148" r="20" fill="var(--ink)"/>
    </svg>
    <p class="brand-name">AMBER MEADOW</p>
    <h1 class="product-name"><span>TOMATO</span><span>RELISH</span></h1>
    <div class="produce-visual" role="img" aria-label="Illustration of fresh tomatoes, onion, garlic and herbs"></div>
    <svg class="label-art" width="426" height="736" viewBox="0 0 426 736">
      <circle cx="97" cy="579" r="63" fill="var(--label)" stroke="var(--ink)" stroke-width="1.6"/>
      <circle cx="97" cy="579" r="55" fill="none" stroke="var(--ink)" stroke-width="0.8"/>
    </svg>
    <p class="claim-badge">POPULAR<br>CHOICE</p>
    <div class="batch-field">
      <span>BATCH<span class="field-line"></span></span>
      <span>DATE<span class="field-line"></span></span>
    </div>
    <p class="tagline">Made with love <span class="heart">&#9829;</span></p>
  </section>

  <section class="label label-5">
    <svg class="label-art" width="426" height="736" viewBox="0 0 426 736">
      <defs>
        <path id="claim-arc" d="M26 176 A50 50 0 0 1 108 122"/>
      </defs>
      <text font-family="Poppins, sans-serif" font-weight="300" font-size="10" letter-spacing="1" fill="var(--ink)">
        <textPath href="#claim-arc">POPULAR CHOICE</textPath>
      </text>
      <path d="M18 182 A58 58 0 0 1 106 110" fill="none" stroke="var(--ink)" stroke-width="1"/>
    </svg>
    <h1 class="product-name"><span>TOMATO</span><span>RELISH</span></h1>
    <div class="logo-spot">
      <span class="logo-dot"></span>
      <span class="logo-name">AMBER MEADOW</span>
    </div>
    <div class="batch-field">
      <span>BATCH<span class="field-line"></span></span>
      <span>DATE<span class="field-line"></span></span>
    </div>
    <p class="tagline">Made with love <span class="heart">&#9829;</span></p>
  </section>

</main>
</body>
</html>
```